New adult online store shopify

I have a new product I'd like to build my shopify store on. It's a product used for foreplay in the bedroom for people who have a temperature play fetish. Testing the boundaries with hot and cold. The glass wands are use to heat wax to put on skin to excite adults I'd like to have a retail store with a log in for wholesalers to log in and place orders
Also needs a plug in to confirm viewers are over 18 years old.
It needs to be classy and descriptive with a clear product message and story but very simple to use
Updates

Reason: Deadline extended 5 days

Reason: looking for more options

Target Market(s)

All adults over 18

Industry/Entity Type

Adult

Colors

Designer to choose colors to be used in the design.

Requirements
Must have
• A customer / wholesale login for wholesale purchases
• Templates for abandoned shopping cart emails
• 18+ only visible
Nice to have
• Customer loyalty programme
Should not have
• Cheap Rude images and comment

```html
<!DOCTYPE html>
<html lang="en">
<head>
<meta charset="utf-8">
<title>Age Check</title>
<link href="https://fonts.googleapis.com/css2?family=Chakra+Petch:wght@500;700&family=Saira+Semi+Condensed:wght@700;800&display=swap" rel="stylesheet">
<style>
  :root {
    --ink: #3a3536;
    --paper: #ffffff;
    --night: #000000;
    --sepia-light: #8a8073;
    --sepia-mid: #4a433b;
    --sepia-dark: #1a1714;
    --signal-red: #f20d0d;
    --text-light: #ffffff;
  }
  * { margin: 0; padding: 0; box-sizing: border-box; }
  html, body {
    width: 1200px;
    height: 674px;
    overflow: hidden;
    background: var(--night);
    font-family: "Chakra Petch", sans-serif;
  }
  .page {
    position: relative;
    width: 1200px;
    height: 674px;
    overflow: hidden;
    background: var(--night);
  }
  .site-header {
    position: absolute;
    top: 0; left: 0;
    width: 1200px;
    height: 78px;
    background: var(--paper);
    font-family: "Saira Semi Condensed", sans-serif;
  }
  .main-nav a {
    position: absolute;
    top: 24px;
    color: var(--ink);
    text-decoration: none;
    font-weight: 700;
    font-size: 20px;
    letter-spacing: 2px;
    line-height: 28px;
    white-space: nowrap;
  }
  .nav-collections { left: 431px; }
  .nav-products { left: 608px; }
  .nav-story { left: 753px; }
  .cart {
    position: absolute;
    left: 934px;
    top: 22px;
    display: flex;
    align-items: center;
    gap: 12px;
    color: var(--ink);
    font-weight: 700;
    font-size: 20px;
    letter-spacing: 2px;
    line-height: 28px;
  }
  .search-icon {
    position: absolute;
    left: 1132px;
    top: 24px;
  }
  .hero-photo {
    position: absolute;
    left: 192px;
    top: 78px;
    width: 816px;
    height: 540px;
    background:
      radial-gradient(ellipse 40% 35% at 48% 38%, var(--sepia-light) 0%, transparent 70%),
      radial-gradient(ellipse 45% 30% at 55% 82%, #9a9080 0%, transparent 75%),
      radial-gradient(ellipse 60% 60% at 50% 50%, var(--sepia-mid) 0%, var(--sepia-dark) 75%, var(--night) 100%);
  }
  .age-question {
    position: absolute;
    left: 0;
    top: 329px;
    width: 1192px;
    text-align: center;
    color: var(--text-light);
    font-family: "Saira Semi Condensed", sans-serif;
    font-weight: 800;
    font-size: 26px;
    line-height: 34px;
    letter-spacing: 3px;
  }
  .age-button {
    position: absolute;
    top: 399px;
    width: 206px;
    height: 58px;
    border-radius: 29px;
    display: flex;
    align-items: center;
    justify-content: center;
    color: var(--text-light);
    text-decoration: none;
    font-family: "Saira Semi Condensed", sans-serif;
    font-weight: 800;
    font-size: 25px;
    letter-spacing: 2px;
  }
  .age-yes { left: 362px; background: var(--signal-red); }
  .age-no { left: 621px; border: 2px solid var(--signal-red); background: transparent; }
  .legal-note {
    position: absolute;
    left: 0;
    top: 620px;
    width: 1200px;
    text-align: center;
    color: var(--text-light);
    font-weight: 500;
    font-size: 13px;
    letter-spacing: 1.6px;
  }
</style>
</head>
<body>
<div class="page">
  <header class="site-header">
    <nav class="main-nav">
      <a class="nav-collections" href="#">COLLECTIONS</a>
      <a class="nav-products" href="#">PRODUCTS</a>
      <a class="nav-story" href="#">OUR STORY</a>
    </nav>
    <div class="cart">
      <svg width="32" height="32" viewBox="0 0 24 24" aria-hidden="true"><path fill="#3a3536" d="M7 18c-1.1 0-2 .9-2 2s.9 2 2 2 2-.9 2-2-.9-2-2-2zM1 2v2h2l3.6 7.6-1.4 2.4c-.1.3-.2.6-.2 1 0 1.1.9 2 2 2h12v-2H7.4c-.1 0-.2-.1-.2-.2v-.1l.9-1.7h7.4c.8 0 1.4-.4 1.7-1l3.6-6.5c.1-.2.2-.3.2-.5 0-.6-.4-1-1-1H5.2l-.9-2H1zm16 16c-1.1 0-2 .9-2 2s.9 2 2 2 2-.9 2-2-.9-2-2-2z"/></svg>
      <span>0 ITEMS</span>
    </div>
    <svg class="search-icon" width="30" height="30" viewBox="0 0 24 24" aria-label="Search"><path fill="#3a3536" d="M15.5 14h-.8l-.3-.3c1-1.1 1.6-2.6 1.6-4.2C16 5.9 13.1 3 9.5 3S3 5.9 3 9.5 5.9 16 9.5 16c1.6 0 3.1-.6 4.2-1.6l.3.3v.8l5 5 1.5-1.5-5-5zm-6 0C7 14 5 12 5 9.5S7 5 9.5 5 14 7 14 9.5 12 14 9.5 14z"/></svg>
  </header>

  <div class="hero-photo" role="img" aria-label="Sepia photograph of a woman leaning on a table covered with lit tea-light candles before a brick wall"></div>

  <h1 class="age-question">ARE YOU AT LEAST 21 YEARS OLD?</h1>
  <a class="age-button age-yes" href="#">YES</a>
  <a class="age-button age-no" href="#">NO</a>

  <p class="legal-note">THIS WEBSITE FACILITATES THE SALE OF GLASS WANDS. WE USE COOKIES TO ASSIST IN VERIFYING AGE.</p>
</div>
</body>
</html>
```